Tidewell Consulting Schedule Of Rates

We need a brochure / proposal for our new company. Our company is a start up based in Australia who provides engineering and sales support to other renewable energy companies. Our brochure is a pitch-deck / sales item that catalogues our key services. We are engineering consultants.

Our website is www.tidewellpartners.com.au. Please review the website to get a feel of colour schemes etc.

We are looking for a strong, trustworthy feel, but the brochure also needs to be sales driven and to the point.

The second page that contains the $30 price point needs to be loud and clear.

The use of relevant icons throughout the document will be viewed favorably.

Please format the tables to look attractive.

The document will need to be in an editable format so content can be edited by us at a later date.

Please feel free to use the pics within the attached word document. The winning design will be provided with updated, clearer images upon request.

Thank you

Target Market(s)

Businesses that either sell or install solar PV and other renewable energy systems in Australia. Most of target market are likely to be electrical contractors.

Industry/Entity Type

Engineering

Colors
0255a3
0492cd
ffffff

Requirements
Must have
• Icons, graphics presentation, Clean and Clear, Business oriented. Sharp sales feel
Nice to have
• solar picture backgrounds maybe
Should not have
• cartoons, over sales driven,

```html
<!DOCTYPE html>
<html lang="en">
<head>
<meta charset="utf-8">
<title>Tidewell Consulting – Schedule Of Rates</title>
<link rel="stylesheet" href="https://fonts.googleapis.com/css2?family=Open+Sans:wght@300;400;700&display=swap">
<style>
  :root {
    --navy: #0255a3;
    --cover-blue: #0a66a8;
    --sky: #0492cd;
    --accent: #3fb1e3;
    --white: #ffffff;
    --ink: #1b1b1b;
    --header-tint: #f4f6f8;
    --backdrop: #eef1f4;
  }
  * { margin: 0; padding: 0; box-sizing: border-box; }
  html, body {
    width: 1200px; height: 804px; overflow: hidden;
    background: var(--backdrop);
    font-family: "Open Sans", Arial, sans-serif;
  }
  .stage { position: relative; width: 1200px; height: 804px; }
  .cover {
    position: absolute; left: 330px; top: 20px;
    width: 540px; height: 764px;
    background: var(--white);
    overflow: hidden;
    box-shadow: 0 6px 24px rgba(0,0,0,0.18);
  }
  .cover__header {
    position: absolute; left: 0; top: 0; width: 100%; height: 196px;
    background: linear-gradient(180deg, var(--white) 0%, var(--header-tint) 100%);
  }
  .brand {
    position: absolute; left: 46px; top: 96px;
    display: flex; align-items: center; gap: 10px;
  }
  .brand__mark { width: 14px; height: 14px; background: var(--sky); }
  .brand__name {
    font-weight: 700; font-size: 26px; color: var(--ink);
    letter-spacing: -0.3px;
  }
  .cover__stripe {
    position: absolute; left: 0; top: 196px; width: 100%; height: 7px;
    background: var(--sky);
  }
  .cover__photo {
    position: absolute; left: 0; top: 203px; width: 100%; height: 230px;
    background: linear-gradient(180deg, #b9d3ea 0%, #8fb6dc 40%, #2f5fa8 75%, #1c4590 100%);
  }
  .cover__pointer { position: absolute; left: 52px; top: 196px; }
  .cover__panel {
    position: absolute; left: 0; top: 433px; width: 100%; height: 331px;
    background: var(--cover-blue);
  }
  .cover__titles { position: absolute; left: 46px; top: 480px; color: var(--white); }
  .cover__kicker { font-weight: 300; font-size: 31px; line-height: 1.2; }
  .cover__title { font-weight: 700; font-size: 33px; color: var(--accent); line-height: 1.25; }
  .cover__range { font-weight: 300; font-size: 22px; color: #cfe6f5; line-height: 1.4; }
  .cover__web {
    position: absolute; right: 0; bottom: 26px;
    background: var(--white); padding: 5px 16px 5px 18px;
    font-size: 10px; color: var(--navy);
  }
  .cover__web b { color: var(--sky); font-weight: 400; }
</style>
</head>
<body>
<main class="stage">
  <article class="cover">
    <div class="cover__header"></div>

    <div class="brand">
      <span class="brand__mark"></span>
      <span class="brand__name">Tidewell Consulting</span>
    </div>

    <div class="cover__stripe"></div>
    <div class="cover__photo" role="img" aria-label="Photo of a technician in a white hard hat installing rooftop solar panels under a blue sky"></div>
    <svg class="cover__pointer" width="60" height="42" viewBox="0 0 60 42" aria-hidden="true">
      <polygon points="0,0 60,0 38,42" fill="var(--sky)"/>
    </svg>

    <div class="cover__panel"></div>

    <div class="cover__titles">
      <p class="cover__kicker">Design &amp; Support Services</p>
      <h1 class="cover__title">Schedule Of Rates</h1>
      <p class="cover__range">Grid and Off Grid 5kW – 10MW</p>
    </div>

    <p class="cover__web">www.<b>tidewell</b>partners.com.au</p>
  </article>
</main>
</body>
</html>
```